business card design for luxurious real estate brand

using the attached logo, i am looking for a 2-sided business card design. the back should be the gold logo on black background. the front needs to include: gold logo, name, phone, email, and website

Industry/Entity Type

real estate

Contact Information for Business Card

logo, name, email, phone, website

Font styles to use
Sans Serif

```html
<!DOCTYPE html>
<html lang="en">
<head>
<meta charset="UTF-8">
<title>Casa Lumera – Business Card</title>
<link rel="stylesheet" href="https://fonts.googleapis.com/css2?family=Montserrat:wght@400;600;700&display=swap">
<style>
  :root {
    --backdrop: #2e2926;
    --card: #151515;
    --card-deep: #0a0a0a;
    --gold: #f7c600;
    --ink-light: #e9e9e9;
    --ink-muted: #bdbdbd;
  }
  * { box-sizing: border-box; margin: 0; padding: 0; }
  html, body { width: 1200px; height: 716px; overflow: hidden; }
  body {
    background: var(--backdrop);
    font-family: "Montserrat", sans-serif;
    display: flex;
    align-items: center;
    justify-content: center;
    gap: 40px;
  }
  .card {
    width: 540px;
    height: 309px;
    position: relative;
    background: linear-gradient(135deg, var(--card) 0%, var(--card) 55%, var(--card-deep) 100%);
    box-shadow: 0 14px 30px rgba(0,0,0,0.5);
    overflow: hidden;
  }
  .wordmark {
    display: flex;
    align-items: center;
    gap: 10px;
    color: var(--gold);
    font-weight: 600;
    text-transform: uppercase;
    letter-spacing: 0.28em;
    white-space: nowrap;
  }
  .wordmark-square {
    width: 12px;
    height: 12px;
    background: var(--gold);
    flex: none;
  }
  .card-front .wordmark {
    position: absolute;
    left: 36px;
    top: 36px;
    font-size: 16px;
  }
  .identity {
    position: absolute;
    left: 36px;
    top: 104px;
    padding-left: 18px;
    border-left: 5px solid var(--gold);
  }
  .identity-name {
    color: var(--gold);
    font-weight: 700;
    font-size: 20px;
    letter-spacing: 0.06em;
    text-transform: uppercase;
    line-height: 1.15;
  }
  .identity-role {
    color: var(--ink-muted);
    font-size: 12px;
    margin-top: 4px;
  }
  .contact-list {
    position: absolute;
    left: 36px;
    bottom: 40px;
    list-style: none;
    display: flex;
    flex-direction: column;
    gap: 7px;
  }
  .contact-item {
    display: flex;
    align-items: center;
    gap: 10px;
    color: var(--ink-light);
    font-size: 12.5px;
  }
  .contact-icon { width: 12px; height: 12px; flex: none; }
  .card-back .wordmark {
    position: absolute;
    right: 40px;
    bottom: 44px;
    font-size: 24px;
    gap: 14px;
  }
  .card-back .wordmark-square { width: 16px; height: 16px; }
</style>
</head>
<body>

  <section class="card card-front" aria-label="Business card front">
    <div class="wordmark"><span class="wordmark-square"></span>Casa Lumera</div>

    <div class="identity">
      <p class="identity-name">Remy Castell</p>
      <p class="identity-role">President</p>
    </div>

    <ul class="contact-list">
      <li class="contact-item">
        <svg class="contact-icon" viewBox="0 0 24 24" aria-hidden="true">
          <path fill="#f7c600" d="M6.6 10.8a15.1 15.1 0 0 0 6.6 6.6l2.2-2.2c.3-.3.7-.4 1-.2 1.1.4 2.3.6 3.6.6.6 0 1 .4 1 1V20c0 .6-.4 1-1 1A17 17 0 0 1 3 4c0-.6.4-1 1-1h3.5c.6 0 1 .4 1 1 0 1.3.2 2.5.6 3.6.1.3 0 .7-.2 1z"/>
        </svg>
        555-204-7781
      </li>
      <li class="contact-item">
        <svg class="contact-icon" viewBox="0 0 24 24" aria-hidden="true">
          <path fill="#f7c600" d="M2 5h20v14H2zm2 2v.5l8 5 8-5V7l-8 5z"/>
        </svg>
        remy@casalumera.com
      </li>
      <li class="contact-item">
        <svg class="contact-icon" viewBox="0 0 24 24" aria-hidden="true">
          <circle cx="12" cy="12" r="9" fill="none" stroke="#f7c600" stroke-width="2.5"/>
          <path d="M3 12h18M12 3c3 3 3 15 0 18M12 3c-3 3-3 15 0 18" fill="none" stroke="#f7c600" stroke-width="1.8"/>
        </svg>
        www.casalumera.com
      </li>
    </ul>
  </section>

  <section class="card card-back" aria-label="Business card back">
    <div class="wordmark"><span class="wordmark-square"></span>Casa Lumera</div>
  </section>

</body>
</html>
```